Stationery design for law/Property/finance business

We need stationery design for a Law/Property/Finance business called Ridgemoor. Logo is attached.
we require a letterhead and with compliments slip.
Would like to see a very simple professional design using the colours of the logo and offset against Charcoal colours. Maybe a charcoal band for header and footer with logo and details appearing in it? Former letterhead attached for examples.
we require the project to be provided in word, pdf and jpeg format.
we require the following details on the stationery:
Cairns Phone: 07 40551926
Weipa Phone: 07 40613847
Mobile: 0491 570 384
Fax: 07 40338172
email: admin@ridgemoorholdings-example.com.au
ABN 51 824 306 917

```html
<!DOCTYPE html>
<html lang="en">
<head>
<meta charset="utf-8">
<title>Ridgemoor Stationery</title>
<link rel="stylesheet" href="https://fonts.googleapis.com/css2?family=Montserrat:wght@500;600;700&family=Grandstander:wght@600&display=swap">
<style>
  :root {
    --backdrop: #b9b9b9;
    --paper: #ffffff;
    --brand-blue: #1f7fc8;
    --brand-aqua: #7fd0c8;
    --wash-blue: #cfe3f3;
    --wash-aqua: #e3f4f1;
    --charcoal: #232323;
    --ink: #222222;
    --rule: #555555;
    --band-text: #ffffff;
  }
  * { box-sizing: border-box; margin: 0; padding: 0; }
  html, body { width: 1200px; height: 1200px; overflow: hidden; }
  body {
    position: relative;
    background: var(--backdrop);
    font-family: "Montserrat", Arial, sans-serif;
    color: var(--ink);
  }
  .sheet { position: absolute; background: var(--paper); }
  .letterhead { left: 334px; top: 79px; width: 517px; height: 732px; }
  .comp-slip { left: 293px; top: 848px; width: 617px; height: 290px; }

  .brand-name {
    position: absolute;
    font-weight: 700;
    color: var(--brand-blue);
    letter-spacing: -0.3px;
    line-height: 1;
  }
  .letterhead .brand-name { left: 46px; top: 44px; font-size: 25px; }
  .comp-slip .brand-name { left: 25px; top: 34px; font-size: 18px; }

  .contact-block { position: absolute; font-weight: 500; line-height: 1; }
  .contact-block .row { display: flex; align-items: center; gap: 4px; position: absolute; left: 0; white-space: nowrap; }
  .contact-block svg { flex: none; }
  .letterhead .contact-block {
    left: 332px; top: 41px; height: 38px; width: 170px;
    border-left: 1px solid var(--rule); font-size: 7px;
  }
  .letterhead .contact-block .row { left: 10px; }
  .letterhead .r1 { top: 5px; } .letterhead .r2 { top: 16px; } .letterhead .r3 { top: 33px; }
  .comp-slip .contact-block { left: 25px; top: 72px; width: 240px; font-size: 9px; }
  .comp-slip .r1 { top: 0; } .comp-slip .r2 { top: 13px; } .comp-slip .r3 { top: 27px; }

  .compliments {
    position: absolute; left: 453px; top: 28px;
    font-family: "Grandstander", "Comic Sans MS", cursive;
    font-weight: 600; font-size: 17px; color: var(--brand-blue);
  }

  .wash {
    position: absolute;
    border-radius: 50%;
    background: radial-gradient(ellipse at 55% 40%, var(--wash-blue) 0%, var(--wash-aqua) 45%, rgba(255,255,255,0) 72%);
  }
  .letterhead .wash { left: 31px; top: 445px; width: 284px; height: 208px; }
  .comp-slip .wash { left: 415px; top: 128px; width: 183px; height: 132px; }

  .contact-band {
    position: absolute; left: 0; right: 0;
    background: var(--charcoal); color: var(--band-text);
    font-weight: 500; line-height: 1;
  }
  .contact-band .item { position: absolute; top: 50%; transform: translateY(-50%); display: flex; align-items: center; gap: 4px; white-space: nowrap; }
  .letterhead .contact-band { top: 697px; height: 16px; font-size: 8px; }
  .comp-slip .contact-band { top: 262px; height: 20px; font-size: 10px; }
  .muted { opacity: .85; margin-left: 3px; }
</style>
</head>
<body>

<svg width="0" height="0" style="position:absolute">
  <symbol id="i-mail" viewBox="0 0 10 10"><rect x="1" y="3" width="8" height="6" fill="none" stroke="currentColor"/><path d="M1 3 L5 6 L9 3" fill="none" stroke="currentColor"/></symbol>
  <symbol id="i-web" viewBox="0 0 10 10"><circle cx="5" cy="5" r="4" fill="none" stroke="currentColor"/><path d="M1 5h8M5 1v8M2.5 2.5q2.5 2.5 5 0M2.5 7.5q2.5-2.5 5 0" fill="none" stroke="currentColor" stroke-width=".7"/></symbol>
  <symbol id="i-mobile" viewBox="0 0 10 10"><rect x="3" y="1" width="4.5" height="8" rx=".8" fill="none" stroke="currentColor"/></symbol>
  <symbol id="i-fax" viewBox="0 0 10 10"><rect x="1" y="4" width="8" height="5" fill="currentColor"/><rect x="3" y="1" width="4" height="3" fill="currentColor"/></symbol>
  <symbol id="i-phone" viewBox="0 0 10 10"><path d="M1 4q4-3 8 0v1.5H7V4.5H3v1H1z M2.5 6h5l1 3h-7z" fill="currentColor"/></symbol>
</svg>

<section class="sheet letterhead">
  <div class="brand-name">Ridgemoor</div>
  <div class="contact-block">
    <div class="row r1"><svg width="8" height="8" style="color:var(--brand-blue)"><use href="#i-mail"/></svg>admin@ridgemoorholdings-example.com.au</div>
    <div class="row r2"><svg width="8" height="8" style="color:var(--brand-blue)"><use href="#i-web"/></svg>www.ridgemoorholdings-example.com.au</div>
    <div class="row r3">ABN 51 824 306 917</div>
  </div>
  <div class="wash" role="img" aria-label="Faint brand wave decoration"></div>
  <div class="contact-band">
    <span class="item" style="left:68px"><svg width="7" height="7"><use href="#i-mobile"/></svg>0491 570 384</span>
    <span class="item" style="left:149px"><svg width="7" height="7"><use href="#i-fax"/></svg>07 40338172</span>
    <span class="item" style="left:234px"><svg width="8" height="7"><use href="#i-phone"/></svg>07 40551926 <span class="muted">(Cairns)</span></span>
    <span class="item" style="left:348px"><svg width="8" height="7"><use href="#i-phone"/></svg>07 40613847 <span class="muted">(Weipa)</span></span>
  </div>
</section>

<section class="sheet comp-slip">
  <div class="brand-name">Ridgemoor</div>
  <div class="compliments">With Compliments</div>
  <div class="contact-block">
    <div class="row r1"><svg width="10" height="10" style="color:var(--brand-blue)"><use href="#i-mail"/></svg>admin@ridgemoorholdings-example.com.au</div>
    <div class="row r2"><svg width="10" height="10" style="color:var(--brand-blue)"><use href="#i-web"/></svg>www.ridgemoorholdings-example.com.au</div>
    <div class="row r3">ABN 51 824 306 917</div>
  </div>
  <div class="wash" role="img" aria-label="Faint brand wave decoration"></div>
  <div class="contact-band">
    <span class="item" style="left:81px"><svg width="9" height="9"><use href="#i-mobile"/></svg>0491 570 384</span>
    <span class="item" style="left:177px"><svg width="9" height="9"><use href="#i-fax"/></svg>07 40338172</span>
    <span class="item" style="left:278px"><svg width="10" height="9"><use href="#i-phone"/></svg>07 40551926 <span class="muted">(Cairns)</span></span>
    <span class="item" style="left:414px"><svg width="10" height="9"><use href="#i-phone"/></svg>07 40613847 <span class="muted">(Weipa)</span></span>
  </div>
</section>

</body>
</html>
```